Orva Business Card

we need a business card for flooring business called Orva Flooring, the design should be black and white. we have 2 locations

Nunawading Showroom
527 Kellerman Road,
Nunawading VIC 3131

Bentleigh Showroom
462 Bramwell Hwy,
Bentleigh VIC 3204

email : sales@orvaflooring.com.au
(03) 9471 2830

Please inform we sell , Laminate, Hybrid, Timber, carpet and commercial flooring

```html
<!DOCTYPE html>
<html lang="en">
<head>
<meta charset="utf-8">
<title>Orva Flooring Business Card</title>
<link href="https://fonts.googleapis.com/css2?family=Poppins:wght@300;400;500&display=swap" rel="stylesheet">
<style>
  :root {
    --stage: #d9d9d9;
    --card-white: #ffffff;
    --card-black: #141414;
    --ink: #111111;
    --ink-soft: #2a2a2a;
    --rule: #111111;
  }
  html, body {
    margin: 0;
    padding: 0;
    width: 1200px;
    height: 900px;
    overflow: hidden;
    background: var(--stage);
    font-family: "Poppins", sans-serif;
    color: var(--ink);
  }
  .stage {
    position: relative;
    width: 1200px;
    height: 900px;
  }
  .card {
    position: absolute;
    top: 150px;
    width: 340px;
    height: 595px;
    box-sizing: border-box;
    box-shadow: 0 6px 18px rgba(0,0,0,0.18);
  }
  .card--front {
    left: 225px;
    background: var(--card-white);
    padding: 62px 40px 40px 48px;
  }
  .card--back {
    left: 635px;
    background: var(--card-black);
  }
  .brand {
    text-align: center;
    font-weight: 300;
    font-size: 46px;
    letter-spacing: 2px;
    line-height: 1.1;
    margin: 0;
  }
  .brand__sub {
    display: block;
    font-size: 22px;
    letter-spacing: 3px;
  }
  .details {
    position: absolute;
    left: 48px;
    right: 30px;
    top: 300px;
    font-size: 14px;
    font-weight: 300;
    line-height: 1.35;
  }
  .contact {
    margin: 0;
    padding: 0;
    list-style: none;
  }
  .contact li {
    display: flex;
    align-items: center;
    gap: 6px;
  }
  .contact svg {
    width: 13px;
    height: 13px;
    flex: none;
  }
  .rule {
    width: 64px;
    height: 0;
    border: 0;
    border-top: 1.5px solid var(--rule);
    margin: 12px 0 14px;
  }
  .showroom {
    margin: 0 0 10px;
  }
  .heading {
    font-weight: 500;
    display: block;
  }
  .services {
    margin: 0;
  }
</style>
</head>
<body>
<main class="stage">
  <section class="card card--front" aria-label="Card front">
    <h1 class="brand">Orva<span class="brand__sub">FLOORING</span></h1>
    <div class="details">
      <ul class="contact">
        <li>
          <svg viewBox="0 0 24 24" aria-hidden="true"><path d="M6.6 10.8a15 15 0 0 0 6.6 6.6l2.2-2.2a1 1 0 0 1 1-.25 11.4 11.4 0 0 0 3.6.57 1 1 0 0 1 1 1V20a1 1 0 0 1-1 1A17 17 0 0 1 3 4a1 1 0 0 1 1-1h3.5a1 1 0 0 1 1 1c0 1.25.2 2.45.57 3.6a1 1 0 0 1-.25 1z" fill="currentColor"/></svg>
          (03) 9471 2830
        </li>
        <li>
          <svg viewBox="0 0 24 24" aria-hidden="true"><rect x="2.5" y="5" width="19" height="14" rx="1.5" fill="none" stroke="currentColor" stroke-width="2"/><path d="M3 6l9 7 9-7" fill="none" stroke="currentColor" stroke-width="2"/></svg>
          sales@orvaflooring.com.au
        </li>
      </ul>
      <hr class="rule">
      <p class="showroom"><span class="heading">Nunawading Showroom</span>527 Kellerman Road,<br>Nunawading VIC 3131</p>
      <p class="showroom"><span class="heading">Bentleigh Showroom</span>462 Bramwell Hwy,<br>Bentleigh VIC 3204</p>
      <hr class="rule">
      <p class="services"><span class="heading">Orva Flooring service</span>Laminate | Hybrid | Timber<br>carpet and commercial flooring</p>
    </div>
  </section>
  <section class="card card--back" role="img" aria-label="Card back: black surface with a repeating embossed brand pattern"></section>
</main>
</body>
</html>
```